Corporate flyer highlighting service offering for PR agency

A corporate flyer is needed for a new service offering that we are doing. The product name is HarborLeap it is a marketing and communications services offering for companies who are getting ready to sell their business. If we are really happy with the designer's work, there will be a great deal more projects. I am looking for a clean design with a few pops of color from my site. https://quillmarsh.partners. I am looking for a good design with data in sections. I am looking for a clean design that feels high-end but not cluttered. Please do not use images of people. Please see the following examples of types of designs I like.
https://www.tackboard.example/pin/839201746530918264/
https://www.tackboard.example/pin/402918375561029847/
https://assets.stockvale.example/corporate-flyer-template-KRTPMB
https://designbrook.example/item/corporate-flyer-template/81046395?s_rank=8
https://assets.stockvale.example/corporate-business-flyer-template-93PX7D

I had to place the project on hold as I choose the wrong type of project and did not get many designs as a result. I am reposting this with an updated brief.

Target Market(s)

Business sellers and brokers

Industry/Entity Type

Marketing for business sellers

Font styles to use
Sans Serif

Requirements
Must have
• Good quality design with content in sections. Clean and high end feeling is a must.
Should not have
• A lot of images of people.

```html
<!DOCTYPE html>
<html lang="en">
<head>
<meta charset="utf-8">
<title>HarborLeap Flyer – Quillmarsh Partners</title>
<link href="https://fonts.googleapis.com/css2?family=Montserrat:wght@500;600;700&family=Open+Sans:ital,wght@0,400;0,600;0,700;1,400;1,600&display=swap" rel="stylesheet">
<style>
:root{
  --bg:#b9bcbe;
  --paper:#ffffff;
  --blue:#1f74c2;
  --blue-mid:#2f86d3;
  --navy:#123f78;
  --sky:#cfe4f7;
  --pale:#eef4fa;
  --green:#7caa4c;
  --grey:#6b6f73;
  --dark:#2a2d31;
  --ink:#3d4146;
}
*{margin:0;padding:0;box-sizing:border-box}
html,body{width:933px;height:1200px;overflow:hidden}
body{background:var(--bg);font-family:"Open Sans",Arial,sans-serif;color:var(--ink);position:relative}
.page-label{position:absolute;font-family:"Montserrat",Arial,sans-serif;font-weight:500;font-size:30px;color:var(--dark);letter-spacing:1px}
.page{position:absolute;width:354px;height:498px;background:var(--paper);overflow:hidden;box-shadow:0 3px 10px rgba(0,0,0,.35)}
.abs{position:absolute}
.body-text{font-size:5.1px;line-height:1.45;color:var(--ink)}
.body-text p+p{margin-top:5px}
.brand{display:flex;flex-direction:column;align-items:center;font-family:"Montserrat",Arial,sans-serif;color:var(--dark)}
.brand .mark{width:13px;height:13px;background:var(--blue);margin-bottom:3px}
.brand .name{font-weight:600;font-size:10px;letter-spacing:.6px}
.brand .sub{font-weight:600;font-size:4.5px;letter-spacing:2px;margin-top:1px}
.footer-bar{position:absolute;left:0;right:0;bottom:0;height:18px;background:var(--blue);color:#fff;font-size:8px;display:flex;align-items:center;justify-content:center}
/* page 1 */
.p1-title{font-family:"Montserrat",Arial,sans-serif;font-weight:700;font-size:31px;line-height:1.05;color:var(--dark);text-align:right;letter-spacing:1px}
.p1-band{background:var(--blue);color:#fff;padding:8px 10px 6px 16px}
.p1-band h2{font-family:"Montserrat",Arial,sans-serif;font-weight:600;font-size:15px;border-bottom:1px solid #fff;padding-bottom:3px;display:inline-block;width:100%}
.p1-band p{font-size:5.4px;font-weight:700;text-align:right;margin-top:6px;line-height:1.4}
.p1-quote{background:var(--navy);color:#fff;font-style:italic;font-weight:600;font-size:5.6px;line-height:1.42;text-align:center;padding:10px 12px}
.hex-label{font-size:3.4px;font-weight:700;fill:#fff;text-anchor:middle;font-family:"Open Sans",Arial,sans-serif}
/* page 2 */
.p2-italic{color:#fff;font-style:italic;font-weight:600;font-size:6.6px;line-height:1.45;text-align:justify}
.p2-heading{font-family:"Montserrat",Arial,sans-serif;font-weight:600;font-size:9px;color:var(--dark);letter-spacing:.3px}
.step{position:absolute;height:19px;display:flex;align-items:center;font-size:6.3px;color:var(--dark)}
.step-num{position:absolute;width:18px;height:18px;border-radius:50%;background:#fff;border:2px solid var(--dark);font-weight:700;font-size:10px;display:flex;align-items:center;justify-content:center;color:var(--dark)}
.url-box{background:var(--grey);color:#fff;font-size:7.6px;padding:3px 24px}
/* page 3 */
.p3-intro{background:var(--blue);color:#fff;font-size:5.6px;line-height:1.4;padding:6px 14px}
.sec-head{font-family:"Montserrat",Arial,sans-serif;font-weight:600;font-size:5.8px;color:var(--dark);line-height:1.2;padding-left:12px;position:relative;margin-bottom:6px}
.sec-head::before{content:"";position:absolute;left:0;top:0;border-left:9px solid var(--blue);border-bottom:9px solid transparent}
.bullets{list-style:none}
.bullets li{position:relative;padding-left:10px;margin-top:5px;font-size:4.7px;line-height:1.4}
.bullets li::before{content:"";position:absolute;left:1px;top:1px;width:5px;height:5px;border-radius:50%;background:var(--blue)}
.bullets li b{color:var(--blue);font-weight:600}
.bullets.small li::before{width:3px;height:3px;top:2px}
.bullets.italic li{font-style:italic;font-weight:600}
.p3-callout{background:var(--blue);border:2px solid var(--pale);outline:2px solid var(--blue);color:#fff;font-style:italic;font-weight:600;font-size:5.6px;line-height:1.4;padding:10px 10px}
/* page 4 */
.p4-quote{color:#fff;font-style:italic;font-weight:600;font-size:9.5px;line-height:1.35}
.p4-attr{color:#fff;font-weight:600;font-size:10px;margin-top:10px}
</style>
</head>
<body>

<div class="page-label" style="left:210px;top:16px">Page 1</div>
<div class="page-label" style="left:652px;top:10px">Page 2</div>
<div class="page-label" style="left:174px;top:1140px">Page 3</div>
<div class="page-label" style="left:633px;top:1146px">Page 4</div>

<!-- PAGE 1 -->
<section class="page" style="left:70px;top:70px">
  <svg class="abs" style="left:0;top:0" width="354" height="498" viewBox="0 0 354 498">
    <defs>
      <linearGradient id="glassBlue" x1="0" y1="1" x2="1" y2="0"><stop offset="0" stop-color="#2a5d9c"/><stop offset="1" stop-color="#9cc6ea"/></linearGradient>
      <linearGradient id="glassGreen" x1="0" y1="0" x2="1" y2="1"><stop offset="0" stop-color="#9ccc5a"/><stop offset="1" stop-color="#3f7a2e"/></linearGradient>
    </defs>
    <polygon points="0,0 22,0 0,36" fill="#e9eaeb"/>
    <polygon points="28,0 170,0 134,62 100,118 30,118 0,68 0,48" fill="#ececec"/>
    <polygon points="62,0 168,0 100,116 62,50" fill="url(#glassBlue)" role="img" aria-label="Photo of a blue glass office tower"/>
    <polygon points="0,40 40,118 0,196" fill="#1f74c2"/>
    <polygon points="36,170 66,118 134,118 164,170 134,222 66,222" fill="url(#glassGreen)" role="img" aria-label="Photo of a green glass building facade"/>
    <polygon points="134,118 230,118 192,184 164,170" fill="#2f86d3"/>
    <polygon points="164,170 192,184 176,224 140,222" fill="#123f78"/>
  </svg>
  <div class="brand abs" style="left:222px;top:22px"><span class="mark"></span><span class="name">QUILLMARSH</span><span class="sub">PARTNERS</span></div>
  <div class="p1-title abs" style="right:22px;top:112px">HARBOR<br>LEAP</div>
  <div class="p1-band abs" style="left:192px;top:225px;width:162px"><h2>HarborLeap</h2><p>provides executives and business owners with clear guidance to unlock non-financial value ahead of an exit.</p></div>
  <div class="body-text abs" style="left:26px;top:238px;width:150px">
    <p>A strong communication and marketing strategy can significantly increase the value of your business leading up to an exit. Buyers are looking to mitigate risk and unlock potential value as a catalyst for clear growth potential.</p>
    <p>Highlighting your company’s success in the marketplace, identifying, and mitigating reputation risks before buyers do, enhancing employee engagement, finding hidden opportunities to boost marketing KPIs and showcasing IP, data, and innovation, can make a significant difference in valuation.</p>
    <p style="font-weight:700;font-style:italic">We design and implement communication and marketing strategies that deliver significant increases in brand awareness, identify reputational risks, and enhance brand perception, helping owners and investors to realize premium values for their companies. We support owners and companies through:</p>
  </div>
  <div class="p1-quote abs" style="left:238px;top:318px;width:116px">“US institutional investors believe that Investor Relations (IR) accounts for a total valuation of 30% in a company’s valuation – from a premium of 10% for “superb” IR to a discount of 20% for “poor” IR. ---Norvane Research Group, “Harnessing IR’s Power to Impact a Company’s Valuation.”</div>
  <svg class="abs" style="left:24px;top:378px" width="210" height="62" viewBox="0 0 210 62">
    <g stroke="#b9d39a" stroke-width="2">
      <polygon points="16,2 36,2 46,19 36,36 16,36 6,19" fill="#8a9196"/>
      <polygon points="56,24 76,24 86,41 76,58 56,58 46,41" fill="#1f74c2"/>
      <polygon points="86,2 106,2 116,19 106,36 86,36 76,19" fill="#8a9196"/>
      <polygon points="126,24 146,24 156,41 146,58 126,58 116,41" fill="#1f74c2"/>
      <polygon points="156,2 176,2 186,19 176,36 156,36 146,19" fill="#8a9196"/>
    </g>
    <text class="hex-label" x="26" y="21">COMPANY</text><text class="hex-label" x="26" y="26">PREPARATION</text>
    <text class="hex-label" x="66" y="48">M&amp;A</text>
    <text class="hex-label" x="96" y="28">IPO</text>
    <text class="hex-label" x="136" y="43">SPINOFF /</text><text class="hex-label" x="136" y="48">DIVESTITURE</text>
    <text class="hex-label" x="166" y="21">NEW</text><text class="hex-label" x="166" y="26">LEADERSHIP</text>
  </svg>
  <div class="body-text abs" style="left:26px;top:446px;width:306px">Few sellers would list their home without first inspecting, repairing broken items, and making updates to highlight the positive aspects – increasing appeal to buyers. However, countless business owners leave money on the table during corporate exits due to a lack of preparation.</div>
  <div class="footer-bar">www.quillmarsh.partners</div>
</section>

<!-- PAGE 2 -->
<section class="page" style="left:509px;top:70px">
  <svg class="abs" style="left:0;top:0" width="354" height="498" viewBox="0 0 354 498">
    <defs>
      <linearGradient id="chartBlue" x1="0" y1="1" x2="1" y2="0"><stop offset="0" stop-color="#7fb3e3"/><stop offset="1" stop-color="#e6f1fb"/></linearGradient>
      <linearGradient id="calcBlue" x1="0" y1="0" x2="1" y2="1"><stop offset="0" stop-color="#3f8fd6"/><stop offset="1" stop-color="#154f92"/></linearGradient>
    </defs>
    <polygon points="210,140 290,0 354,0 354,140" fill="url(#chartBlue)" role="img" aria-label="Photo of rising financial bar charts"/>
    <polygon points="200,130 276,0 284,0 206,134" fill="#5a5d60"/>
    <polygon points="0,123 112,123 90,160 0,160" fill="#3d4043"/>
    <polygon points="0,140 354,140 354,260 290,260 0,260" fill="url(#calcBlue)" role="img" aria-label="Photo of a hand using a calculator over financial reports"/>
    <polygon points="160,140 354,140 354,230 216,230 168,150" fill="#1f74c2"/>
    <polygon points="300,230 354,230 354,300 340,300" fill="#3d4043"/>
    <polygon points="0,430 0,470 40,470" fill="#1f74c2"/>
    <polygon points="0,470 0,498 60,498" fill="#2f86d3"/>
  </svg>
  <div class="body-text abs" style="left:24px;top:30px;width:222px;font-size:5.4px">Our team of executive-level communications and marketing experts brings deep buy and sell-side experience. We have played critical roles in the acquisition, integration, and disposition process. Our mix of financial services expertise combined with decades of experience leading internal and external communications, marketing and investor relations teams gives us a unique perspective on identifying and unlocking non-financial areas of value and mitigating non-financial risks before exit.</div>
  <div class="p2-italic abs" style="left:182px;top:162px;width:152px">While accounting and investment banking teams are hard at work increasing value from a financial perspective, we help organizations enhance their valuation by identifying areas that will appeal most to buyers and ensuring those elements of your business are visible and memorable to those who matter most.</div>
  <div class="p2-heading abs" style="left:30px;top:311px">WE HELP COMPANIES INCREASE VALUATION BY:</div>
  <div class="step" style="left:118px;top:338px;width:236px;background:var(--sky);padding-left:34px">Highlighting value in a clear and visible way</div>
  <div class="step" style="left:102px;top:366px;width:252px;background:#fff;padding-left:34px;box-shadow:0 0 0 .5px #ddd">Streamlining the exit process</div>
  <div class="step" style="left:86px;top:392px;width:268px;background:var(--sky);padding-left:26px">Identifying potential risks and suggesting mitigation measures</div>
  <div class="step" style="left:70px;top:418px;width:284px;background:#fff;padding-left:20px">Creating a polished presence in the market ahead of buyer interest</div>
  <svg class="abs" style="left:40px;top:330px" width="100" height="110" viewBox="0 0 100 110">
    <polygon points="80,8 94,8 30,110 16,110" fill="#3d4043"/>
    <polygon points="72,8 80,8 16,110 4,110" fill="#1f74c2"/>
  </svg>
  <div class="step-num" style="left:113px;top:337px">1</div>
  <div class="step-num" style="left:92px;top:366px">2</div>
  <div class="step-num" style="left:72px;top:396px">3</div>
  <div class="step-num" style="left:50px;top:429px">4</div>
  <div class="brand abs" style="left:64px;top:460px"><span class="mark" style="width:10px;height:10px"></span><span class="name" style="font-size:7.5px">QUILLMARSH</span><span class="sub" style="font-size:3.6px">PARTNERS</span></div>
  <div class="url-box abs" style="left:162px;top:474px;width:192px">www.quillmarsh.partners</div>
</section>

<!-- PAGE 3 -->
<section class="page" style="left:70px;top:632px">
  <div class="p3-intro abs" style="left:0;top:0;width:354px;height:50px">HarborLeap provides executives and business owners with clear guidance to unlock value ahead of an exit. Our non-disruptive, ala-carte process enables us to work with sellers on specific areas or to do a complete analysis and recommendation and can include:</div>
  <div class="abs" style="left:0;top:50px;width:0;height:0;border-top:28px solid #fff;border-left:60px solid var(--pale)"></div>
  <div class="abs" style="left:14px;top:62px;width:156px">
    <div class="sec-head">BRAND ANALYSIS AND<br>RECOMMENDATIONS</div>
    <div class="body-text" style="font-size:4.7px">Strong brands command a higher valuation. We conduct a brand analysis, providing clear and detailed recommendations to enhance your value proposition and help you stand out from the crowd:</div>
    <ul class="bullets">
      <li><b>Current external position among competitors –</b><br>We look at how your brand measures up based on external competitive analysis, positioning in the media and analyst community, and across other digital channels.</li>
      <li><b>Physical brand image –</b><br>A little bit of paint and updated fixtures can go a long way when increasing the value of a home. The same is true for businesses. Our audit evaluates non-disruptive steps your company can take to enhance your brand look and feel before sale.</li>
      <li><b>Employee brand perception –</b><br>We conduct a high-level external audit with recommendations to enhance engagement for current and prospective employees.</li>
      <li><b>Customer brand perception –</b><br>We conduct a high-level external audit showcasing how customers perceive your brand in the market. We then provide recommendations for enhancing engagement and maximizing value.</li>
    </ul>
  </div>
  <div class="p3-callout abs" style="left:30px;top:318px;width:150px">A 5% increase in customer retention correlates with at least a 25% increase in profit, according to an analysis by Calder &amp; Finch.<br><br>It costs 5 times more to acquire a new customer than to retain a current one and 16 times more to get new customers to the same spending level as existing ones.</div>
  <div class="abs" style="left:190px;top:56px;width:1px;height:390px;background:#d5d8db"></div>
  <div class="abs" style="left:196px;top:62px;width:146px">
    <div class="sec-head">DIGITAL AND TRADITIONAL MARKETING<br>ANALYSIS AND RECOMMENDATIONS</div>
    <div class="body-text" style="font-size:4.5px">It’s about your valuation. Full and fair valuation requires a clear, compelling investment case articulated consistently to the right audience at the right time. Messaging to maximize your value in an acquisition or an IPO is quite different from typical selling messages for prospects, customers, or features and benefits for press and analysts. We understand the issues and speak the right language to maximize perception of value with key decision makers.</div>
    <ul class="bullets small italic">
      <li>Review and recommendations of key messaging and value proposition</li>
      <li>Analysis and recommendations to highlight data, IP, and innovation</li>
      <li>Analysis and recommendations to position key executives likely to remain with the company as thought leaders</li>
      <li>Analysis and recommendations to build employee engagement and retention enhancing your most valuable asset – your team</li>
    </ul>
    <div class="sec-head" style="margin-top:10px">MEDIA AND ANALYST STRATEGY<br>DEVELOPMENT</div>
    <div class="body-text" style="font-size:4.5px">Positive articles and inclusion in analyst reports pack a powerful punch when preparing your business for sale. We work with clients to develop a media strategy that goes beyond brand awareness, leveraging media to build a digital history of third-party validation targeted to enhance appeal to prospective buyers while generating traffic and connections.</div>
    <ul class="bullets small italic">
      <li>Positioning to media and analyst community creating third party validation</li>
      <li>Key angle recommendations</li>
      <li>Announcement timeline and strategy planning to maximize media value of news</li>
    </ul>
    <div class="sec-head" style="margin-top:10px">“WHITE HAT/BLACK HAT REVIEW”</div>
    <div class="body-text" style="font-size:4.5px">We take a buyer’s communications and marketing approach to analyzing the client company and provide a punch list of things a potential buyer is likely to ask about in due diligence from a communications and reputation standpoint to ensure that when buyers start screening for sellers, the client company has the upper hand.</div>
  </div>
  <svg class="abs" style="left:0;top:440px" width="354" height="58" viewBox="0 0 354 58">
    <polygon points="0,20 0,58 90,58" fill="#1f74c2"/>
    <polygon points="250,58 354,0 354,58" fill="#1f74c2"/>
    <polygon points="210,58 354,20 354,30 250,58" fill="#123f78"/>
  </svg>
  <div class="brand abs" style="left:120px;top:452px"><span class="mark" style="width:10px;height:10px"></span><span class="name" style="font-size:7.5px">QUILLMARSH</span><span class="sub" style="font-size:3.6px">PARTNERS</span></div>
</section>

<!-- PAGE 4 -->
<section class="page" style="left:509px;top:632px">
  <svg class="abs" style="left:0;top:0" width="354" height="498" viewBox="0 0 354 498">
    <defs>
      <linearGradient id="towerBlue" x1="0" y1="0" x2="1" y2="1"><stop offset="0" stop-color="#dbe9f6"/><stop offset=".5" stop-color="#6d9fd0"/><stop offset="1" stop-color="#1c4f8c"/></linearGradient>
      <linearGradient id="cityFade" x1="0" y1="0" x2="0" y2="1"><stop offset="0" stop-color="#ffffff"/><stop offset="1" stop-color="#dfe3e7"/></linearGradient>
    </defs>
    <polygon points="0,0 230,0 194,110 0,110" fill="#1f74c2"/>
    <polygon points="230,0 354,0 354,150 244,150 196,110" fill="url(#towerBlue)" role="img" aria-label="Photo of glass skyscrapers against a blue sky"/>
    <polygon points="320,210 354,160 354,260" fill="#1f74c2"/>
    <rect x="0" y="370" width="354" height="128" fill="url(#cityFade)" role="img" aria-label="Faint photo of a city skyline"/>
    <polygon points="0,470 0,498 354,498 354,440 260,498" fill="#1f74c2"/>
  </svg>
  <div class="abs" style="left:16px;top:20px;width:172px">
    <div class="p4-quote">“Strategy without tactics is the slowest route to victory. Tactics without strategy is the noise before defeat.”</div>
    <div class="p4-attr">– Aldo Merrin</div>
  </div>
  <div class="body-text abs" style="left:20px;top:126px;width:186px;font-weight:600;font-size:4.9px">Once the analysis is complete, we deliver actionable intelligence and recommendations to help leaders identify and quickly unlock areas that will boost value and appeal to prospective buyers. Work products include:</div>
  <ul class="bullets abs" style="left:18px;top:160px;width:270px">
    <li><b>Gap Assessment –</b><br>We provide a comprehensive seller report providing analysis and actionable recommendations to increase your valuation while identifying and mitigating non-financial risks.</li>
    <li style="margin-top:8px"><b>Strategic Roadmap –</b><br>Clients are given an actionable tactical roadmap based on the recommendation provided. Organizations can choose to implement key areas or include this powerful guide as part of their presentation to prospective buyers to highlight latent potential. The roadmap provides actionable steps buyers can take upon close as they make their case for your business with their investment committees.</li>
  </ul>
  <div class="body-text abs" style="left:20px;top:272px;width:316px;font-size:4.7px">
    <p>Once the strategy integration roadmap is complete, your team can implement it on your timeline, we can work with your team providing guidance and executive-level support, or we can fully execute deliverables with our robust capabilities and team.</p>
    <p>Our value proposition, based on delivering outcomes rather than just outputs, means that you receive the benefit and capability of deeply experienced corporate communications leaders without adding headcount or the time to identify, recruit, onboard and retain a new team member.</p>
    <p>We help organizations enhance their valuation by identifying areas that will appeal most to buyers and ensuring those elements of your business are visible and memorable to those who matter most.</p>
    <p>HarborLeap helps sellers maximize valuation and unlock hidden potential ahead of an exit – ensuring money is not left on the table.</p>
  </div>
  <div class="brand abs" style="left:132px;top:402px"><span class="mark" style="width:11px;height:11px"></span><span class="name" style="font-size:8.5px">QUILLMARSH</span><span class="sub" style="font-size:3.8px">PARTNERS</span></div>
</section>

</body>
</html>
```